Hello everyone,
I need someone to design a Business Card for my new company. It's called Nordavela and we give procurement services of Chilean Salmon and Seafood in General. More specifically we are purchasing agents, quality inspectors and we help with general papework and logistics. Maybe in the future can open to some agriculture items such as Meat, Dairy Products and Fruits.
All this focused in international clients that cannot have the support they need when buying items from Chile.
A main concept is reliability.

Thank you in advance.

Estanislao.

Target Market(s)

Salmon and Seafood Importers from all world.

Industry/Entity Type

Business

Contact Information for Business Card

The Name: Estanislao Ferrada Quiroz
My Mobile: +56 9 47315268
My Location: Lago serena, Chile

Font styles to use
Serif
Sans Serif

Requirements
Must have
• The company name and a logo.
Nice to have
• Some full color on the back side.
Should not have
• No modern shapes. Just a rectangular business card. Remember that has to be accepted by a lot of different cultures, even senior Japanese clients.

```html
<!DOCTYPE html>
<html lang="en">
<head>
<meta charset="utf-8">
<title>Nordavela Business Card</title>
<link href="https://fonts.googleapis.com/css2?family=EB+Garamond:wght@400;500&display=swap" rel="stylesheet">
<style>
  :root {
    --page-bg: #eef1f2;
    --card-bg: #cfd8bb;
    --ink: #1f2a17;
    --rule: #a9bf72;
  }
  * { box-sizing: border-box; margin: 0; padding: 0; }
  html, body {
    width: 1200px;
    height: 1110px;
    overflow: hidden;
    background: var(--page-bg);
    font-family: "EB Garamond", Georgia, serif;
    color: var(--ink);
  }
  .card {
    position: absolute;
    left: 330px;
    width: 553px;
    height: 324px;
    background: var(--card-bg);
    text-align: center;
  }
  .card--front { top: 157px; }
  .card--back { top: 614px; }
  .mark-dot {
    position: absolute;
    left: 50%;
    transform: translateX(-50%);
    width: 10px;
    height: 10px;
    border-radius: 50%;
    background: var(--ink);
  }
  .card--front .mark-dot { top: 138px; }
  .card--back .mark-dot { top: 100px; }
  .brand-name {
    position: absolute;
    left: 0;
    right: 0;
    top: 158px;
    font-size: 38px;
    font-weight: 400;
    letter-spacing: 0.3px;
    text-transform: uppercase;
    line-height: 1;
  }
  .holder-name {
    position: absolute;
    left: 0;
    right: 0;
    top: 124px;
    font-size: 35px;
    font-weight: 400;
    line-height: 1;
  }
  .holder-rule {
    position: absolute;
    left: 101px;
    right: 98px;
    top: 162px;
    height: 1px;
    background: var(--rule);
  }
  .contact {
    position: absolute;
    left: 0;
    right: 0;
    top: 255px;
    font-size: 16px;
    line-height: 1.05;
  }
</style>
</head>
<body>
  <section class="card card--front">
    <span class="mark-dot"></span>
    <p class="brand-name">Nordavela</p>
  </section>

  <section class="card card--back">
    <span class="mark-dot"></span>
    <h1 class="holder-name">Estanislao Ferrada Quiroz</h1>
    <div class="holder-rule"></div>
    <p class="contact">+56 9 47315268<br>Lago serena, Chile</p>
  </section>
</body>
</html>
```